A small boutique Accounting and Mortgage Broking firm needs a business card design

Quorvel is a Brisbane based boutique accounting and mortgage broking firm. We offer a range of extensive financial services like accounting, tax consulting, book-keeping and mortgage broking.
We need a business card that stands out. The content can stay as it is on the existing card unless you recommend us to change anything on it for a better design.
Please remove the mobile number and give us a suitable format to change the details like email address and name.
Industry/Entity Type
Business
Contact Information for Business Card
Dalian Okoruwe
Quorvel Group Pty Ltd
3/412 Brackwin Rd Ferncliff QLD 4190
PO Box 829 Ferncliff QLD 4190
T 07 3184 5526
F 07 3952 1087
E dokoruwe@quorvel.net.au
Accountants Tax Agents, Mortgage Brokers
www.quorvel.net.au
Look and feel
Each slider illustrates characteristics of the customer's brand and the style your logo design should communicate.

```html
<!DOCTYPE html>
<html lang="en">
<head>
<meta charset="utf-8">
<title>Quorvel Business Card</title>
<link rel="stylesheet" href="https://fonts.googleapis.com/css2?family=Open+Sans:wght@300;400;600;700&display=swap">
<style>
  :root {
    --bg: #3a3a3c;
    --card-white: #f2f2f2;
    --card-white-edge: #e4e4e4;
    --brand-green: #76bc3a;
    --ink: #333537;
    --ink-soft: #4a4c4e;
    --white: #ffffff;
  }
  * { box-sizing: border-box; margin: 0; padding: 0; }
  html, body { width: 1200px; height: 1000px; overflow: hidden; }
  body {
    background: var(--bg);
    font-family: "Open Sans", Arial, sans-serif;
    position: relative;
  }
  .card {
    position: absolute;
    left: 250px;
    width: 700px;
    height: 400px;
    border-radius: 30px;
    overflow: hidden;
  }
  /* Contact side */
  .card-contact {
    top: 70px;
    background: linear-gradient(135deg, var(--white) 0%, var(--card-white) 55%, var(--card-white-edge) 100%);
  }
  .contact-brand {
    position: absolute;
    left: 56px; top: 172px;
    font-weight: 600; font-size: 40px; line-height: 1;
    color: var(--ink);
  }
  .contact-details {
    position: absolute;
    left: 360px; top: 58px;
    color: var(--ink-soft);
  }
  .person-name {
    color: var(--brand-green);
    font-size: 26px; font-weight: 400;
    margin-bottom: 8px;
  }
  .company-name {
    font-size: 15px; font-weight: 700; color: var(--ink);
    margin-bottom: 14px;
  }
  .detail-row {
    display: flex; gap: 14px;
    font-size: 15px; line-height: 21px;
    margin-bottom: 10px;
  }
  .detail-label {
    width: 14px; color: var(--brand-green); font-weight: 700;
  }
  /* Brand side */
  .card-brand {
    top: 530px;
    background: var(--brand-green);
  }
  .brand-wordmark {
    position: absolute;
    left: 100px; top: 96px;
    font-weight: 600; font-size: 84px; line-height: 1;
    color: var(--ink);
  }
  .tagline {
    position: absolute;
    left: 100px; top: 212px;
    font-size: 38px; font-weight: 300; color: var(--ink);
    letter-spacing: 1px;
    white-space: nowrap;
  }
  .website {
    position: absolute;
    left: 290px; top: 272px;
    font-size: 20px; font-weight: 700; color: var(--ink);
  }
  .services {
    position: absolute;
    left: 100px; top: 318px;
    display: flex; gap: 30px;
    font-size: 20px; color: var(--white);
  }
</style>
</head>
<body>
  <section class="card card-contact">
    <p class="contact-brand">Quorvel</p>
    <div class="contact-details">
      <p class="person-name">Dalian Okoruwe</p>
      <p class="company-name">Quorvel Group Pty Ltd</p>
      <div class="detail-row"><span class="detail-label">A</span><span>3/412 Brackwin Rd<br>Ferncliff QLD 4190</span></div>
      <div class="detail-row"><span class="detail-label">P</span><span>PO Box 829 Ferncliff<br>QLD 4190</span></div>
      <div class="detail-row"><span class="detail-label">T</span><span>07 3184 5526</span></div>
      <div class="detail-row"><span class="detail-label">F</span><span>07 3952 1087</span></div>
      <div class="detail-row"><span class="detail-label">E</span><span>dokoruwe@quorvel.net.au</span></div>
    </div>
  </section>

  <section class="card card-brand">
    <p class="brand-wordmark">Quorvel</p>
    <p class="tagline">CLARITY. CARE. PROGRESS.</p>
    <p class="website">www.quorvel.net.au</p>
    <div class="services">
      <span>Accountants</span>
      <span>Tax Agents</span>
      <span>Mortgage Brokers</span>
    </div>
  </section>
</body>
</html>
```